Labels for an activated Charcoal Facial Wash, Scrub and Mask

We need a new label design for a new line of Facial products. The product, falls under our Brand Dovelin and is based on Activated Charcoal. Activated Black Charcoal Facial wash (250ml), Activated Black Charcoal Mask (100gms) and Activated Black Charcoal face scrub (100gms). We would like to see designs that are modern, clean and must communicate natural products.

```html
<!DOCTYPE html>
<html lang="en">
<head>
<meta charset="utf-8">
<title>Dovelin Activated Carbon Labels</title>
<link rel="stylesheet" href="https://fonts.googleapis.com/css2?family=Alegreya+Sans:wght@400;700&display=swap">
<style>
  :root {
    --ink: #231f20;
    --paper: #ffffff;
    --leaf: #7cb32a;
    --stone: #c9c9cb;
    --stone-soft: rgba(201,201,203,0);
    --bamboo: #6f9a2a;
    --bamboo-dark: #3d5a14;
    --gold: #8a8566;
    --edge: #b9b9b9;
  }
  * { margin: 0; padding: 0; box-sizing: border-box; }
  html, body { width: 1200px; height: 1199px; overflow: hidden; background: var(--paper); }
  body { position: relative; font-family: "Alegreya Sans", sans-serif; color: var(--ink); }

  .label {
    position: absolute; top: 293px; width: 290px; height: 613px;
    background: var(--paper);
    border-left: 1px solid var(--edge); border-right: 1px solid var(--edge);
    overflow: hidden;
  }
  .label--wash { left: 97px; }
  .label--mask { left: 457px; }
  .label--scrub { left: 812px; }

  .cap-band { position: absolute; left: 0; right: 0; height: 46px; background: var(--ink); }
  .cap-band--top { top: 0; }
  .cap-band--bottom { bottom: 0; height: 46px; color: var(--paper);
    display: flex; align-items: center; justify-content: center; font-size: 22px; }
  .green-rule { position: absolute; left: 0; right: 0; height: 3px; background: var(--leaf); }
  .green-rule--top { top: 53px; }
  .green-rule--bottom { top: 556px; }

  .product-name {
    position: absolute; left: 0; right: 0; top: 95px; height: 100px;
    display: flex; align-items: center; justify-content: center; text-align: center;
    font-weight: 700; font-size: 50px; line-height: 49px; letter-spacing: 0.5px;
  }

  .stones { position: absolute; left: 0; right: 0; }
  .stones--top { top: 192px; height: 66px;
    background: radial-gradient(ellipse 60% 80% at 50% 100%, var(--stone), var(--stone-soft)); }
  .stones--bottom { top: 434px; height: 62px;
    background: radial-gradient(ellipse 45% 80% at 50% 0%, var(--stone), var(--stone-soft)); }

  .brand-band {
    position: absolute; left: 0; right: 0; top: 256px; height: 179px; background: var(--ink);
  }
  .bamboo { position: absolute; top: 0; height: 100%;
    background: linear-gradient(90deg, var(--bamboo-dark), var(--bamboo), var(--leaf), var(--bamboo-dark)); }
  .bamboo--left { left: 2px; width: 43px; }
  .bamboo--right { right: 0; width: 53px; }
  .brand-name {
    position: absolute; left: 45px; right: 53px; top: 0; height: 100%;
    display: flex; align-items: center; justify-content: center;
    color: var(--gold); font-size: 24px; letter-spacing: 6px; font-weight: 400;
  }

  .claim {
    position: absolute; left: 0; right: 0; top: 482px; text-align: center;
    font-size: 21px; line-height: 24px;
  }
</style>
</head>
<body>
  <section class="label label--wash">
    <div class="cap-band cap-band--top"></div>
    <div class="green-rule green-rule--top"></div>
    <h2 class="product-name">WASH<br>GEL</h2>
    <div class="stones stones--top" role="img" aria-label="Photo of grey charcoal granules"></div>
    <div class="brand-band">
      <div class="bamboo bamboo--left" role="img" aria-label="Photo of green bamboo stalks"></div>
      <div class="brand-name">DOVELIN</div>
      <div class="bamboo bamboo--right" role="img" aria-label="Photo of a curled lucky bamboo stem"></div>
    </div>
    <div class="stones stones--bottom" role="img" aria-label="Photo of scattered charcoal granules"></div>
    <p class="claim">with activated<br>black carbon</p>
    <div class="green-rule green-rule--bottom"></div>
    <div class="cap-band cap-band--bottom">250 ml</div>
  </section>

  <section class="label label--mask">
    <div class="cap-band cap-band--top"></div>
    <div class="green-rule green-rule--top"></div>
    <h2 class="product-name">MASK</h2>
    <div class="stones stones--top" role="img" aria-label="Photo of grey charcoal granules"></div>
    <div class="brand-band">
      <div class="bamboo bamboo--left" role="img" aria-label="Photo of green bamboo stalks"></div>
      <div class="brand-name">DOVELIN</div>
      <div class="bamboo bamboo--right" role="img" aria-label="Photo of a curled lucky bamboo stem"></div>
    </div>
    <div class="stones stones--bottom" role="img" aria-label="Photo of scattered charcoal granules"></div>
    <p class="claim">with activated<br>black carbon</p>
    <div class="green-rule green-rule--bottom"></div>
    <div class="cap-band cap-band--bottom">100 g</div>
  </section>

  <section class="label label--scrub">
    <div class="cap-band cap-band--top"></div>
    <div class="green-rule green-rule--top"></div>
    <h2 class="product-name">FACIAL<br>SCRUB</h2>
    <div class="stones stones--top" role="img" aria-label="Photo of grey charcoal granules"></div>
    <div class="brand-band">
      <div class="bamboo bamboo--left" role="img" aria-label="Photo of green bamboo stalks"></div>
      <div class="brand-name">DOVELIN</div>
      <div class="bamboo bamboo--right" role="img" aria-label="Photo of a curled lucky bamboo stem"></div>
    </div>
    <div class="stones stones--bottom" role="img" aria-label="Photo of scattered charcoal granules"></div>
    <p class="claim">with activated<br>black carbon</p>
    <div class="green-rule green-rule--bottom"></div>
    <div class="cap-band cap-band--bottom">100 g</div>
  </section>
</body>
</html>
```